Creative Realtor Business Card Design

I need a creative business card.... I would like it to be larger than the normal size...heavy stock.... colorful...
As you are probably aware, there are tons of realtors, and most of their cards ALL look alike.. potential clients are looking for agents that are professional, but are different.
Cards are a form of advertising and I need your help to make mine stand out in a professional, classy way.
I don't need to use the harbor sage realty logo, my personal logo is MORE important for branding purposes. OR..what is your opinion?
YOU DESIGN FOR ME PLEASE! If I could do what you do I would.... I can't and I need your professional help.

                                        If you think I need the card to be double sided so it doesn't look busy by all means I will happily accept double sided. 

I am very interested in a more "creative" card than a standard run of the mill realtor card.    I care about my clients LONG after the sale has closed!

                                   

THANK YOU SO MUCH FOR YOUR EFFORTS AND TALENTS....I APPRECIATE IT SO MUCH! 

                                        Would it be possible to use my theme of my logo to design my card?

                                            Where Keys Meet Kindred Spirits

                              

 

Please make cards larger size .... See this link for ideas that appeal to me. Thank you for your interest.

https://www.lookwidely.example/find?q=examples+of+unique+business+cards&mode=img&ref=7QpL2xV9

I want my card to stand out in size and design...

Thank you so much for your hard work for me.

Lorna

 

Reason: I learned that many designers are very busy. I am providing more time and money in hopes that designers will find it an attractive enough challenge to participate. My business cards are one of my most important marketing materials...I NEED THEM TO BE DISTINCTIVE, CLASSY, and INFORMATIVE. Thank you SO MUCH....and I will be anxiously awaiting your great designs... Lorna

Hello Designers,

Thank you to all you creative people that have kindly offered to submit your creative design(s) for my business card.  I view your designs as your creative artwork. I am anxious to see where your creativity leads you.

I wanted to share with you that my logo was something I personally designed after being in business for 3  years. ( I did have to have a professionals like yourselves draw it for me). The design and logo captured perfectly how I felt about my work ...helping individuals, such as you, find a home.  A house is easy to find, but a home is a place that has "good" energy ... a place where you feel comfortable and can grow.  A place that just "Feels right!"  It's one of those things that you just KNOW when it is right! 

I hope by sharing this bit of information about me can help you creatively design my card for me...I care for my clients LONG after the transaction has closed and they are in their home. Thank you again for taking the time to work on my design. I have been adding money so that your time spent on my card is worth it.

I do need my card soon...so please, if you have a design...submit it!

Kind Regards,

Lorna

Target Market(s)

I have a variety of clients from a mobile home of $35,000 to an estate property for $5M. I feel comfortable working with all types of people...I love my job...I love helping people find the right home because we all know how our home environment affects our well being.

Industry/Entity Type

Advertising

Contact Information for Business Card

Lorna Pratley, Realtor
Harbor Sage Realty
"Where Keys Meet Kindred Spirits"
www.lornanestfinder.example
lpratley@mailbarn.example
(555) 418-2093
BRE #04872351, Exp. 8/15

Colors

Designer to choose colors to be used in the design.

Requirements
Must have
• By law, my license number information MUST be on my card.
Nice to have
• I would love card to be memorable...if that is possible for a business card. Also, I would like my card to be larger than the average card. Not sure that is possible either.

```html
<!DOCTYPE html>
<html lang="en">
<head>
<meta charset="utf-8">
<title>Lorna Pratley – House Card</title>
<link href="https://fonts.googleapis.com/css2?family=Kaushan+Script&family=Tinos:ital,wght@0,400;0,700;1,400&display=swap" rel="stylesheet">
<style>
  :root {
    --stage: #000000;
    --red-deep: #5c0c10;
    --red-mid: #9a1c22;
    --red-bright: #e01f28;
    --card-white: #ffffff;
    --outline: #8b1a1e;
    --ink: #222222;
    --accent-green: #1a9e4a;
    --text-light: #ffffff;
  }
  html, body {
    margin: 0;
    padding: 0;
    width: 1200px;
    height: 1000px;
    overflow: hidden;
    background: var(--stage);
  }
  .canvas {
    display: block;
    width: 1200px;
    height: 1000px;
  }
  .greeting {
    font-family: "Kaushan Script", cursive;
    font-size: 66px;
    fill: var(--text-light);
  }
  .brand-name {
    font-family: "Tinos", serif;
    font-weight: 700;
    font-size: 27px;
    fill: var(--ink);
  }
  .agent-name {
    font-family: "Tinos", serif;
    font-size: 27px;
    fill: var(--text-light);
  }
  .agent-role {
    font-family: "Tinos", serif;
    font-size: 16.5px;
    fill: var(--text-light);
  }
  .contact {
    font-family: "Tinos", serif;
    font-size: 13px;
    fill: var(--text-light);
  }
  .contact-strong {
    font-family: "Tinos", serif;
    font-weight: 700;
    font-size: 12.5px;
    fill: var(--text-light);
  }
  .tagline {
    font-family: "Tinos", serif;
    font-style: italic;
    font-size: 16.5px;
    fill: var(--text-light);
  }
  .icon-tile { fill: var(--card-white); }
  .icon-line {
    fill: none;
    stroke: var(--accent-green);
    stroke-width: 1.3;
  }
</style>
</head>
<body>
<svg class="canvas" viewBox="0 0 1200 1000" xmlns="http://www.w3.org/2000/svg">
  <defs>
    <linearGradient id="red-sheen-front" x1="0" y1="0" x2="1" y2="0">
      <stop offset="0" stop-color="var(--red-deep)"/>
      <stop offset="0.38" stop-color="var(--red-bright)"/>
      <stop offset="0.75" stop-color="var(--red-mid)"/>
      <stop offset="1" stop-color="var(--red-deep)"/>
    </linearGradient>
    <linearGradient id="red-sheen-heart" x1="0" y1="0" x2="1" y2="0">
      <stop offset="0" stop-color="var(--red-deep)"/>
      <stop offset="0.36" stop-color="var(--red-bright)"/>
      <stop offset="0.72" stop-color="var(--red-mid)"/>
      <stop offset="1" stop-color="var(--red-deep)"/>
    </linearGradient>
  </defs>

  <!-- Front of card -->
  <g class="card-front">
    <path fill="url(#red-sheen-front)"
      d="M382,228 L382,215 L456,215 L456,285 L575,385
         C602,406 592,426 560,426 L520,427
         C532,600 425,758 335,800 C305,812 268,812 238,800
         C148,760 46,620 48,470 L48,422 L28,420
         C-2,416 -6,395 16,378 L190,236
         C240,196 322,190 382,228 Z"/>
    <text class="greeting" x="296" y="523" text-anchor="middle">Hi There!</text>
  </g>

  <!-- Back of card -->
  <g class="card-back">
    <path fill="var(--card-white)" stroke="var(--outline)" stroke-width="5"
      d="M740,285 L740,210 L815,210 L815,225
         C880,180 1000,178 1060,232 L1180,346
         C1210,376 1196,410 1160,410 L1147,410
         C1155,600 1050,760 960,796 C920,810 882,810 842,796
         C752,760 676,620 680,420 L642,416
         C606,410 600,386 620,370 Z"/>

    <path fill="url(#red-sheen-heart)"
      d="M912,435 C880,402 780,400 722,428
         C690,450 684,505 690,570
         C702,680 800,782 860,802 C890,812 920,812 950,800
         C1030,770 1110,690 1134,590
         C1150,520 1145,462 1110,430
         C1062,402 950,402 912,435 Z"/>

    <g class="brand-mark">
      <rect x="812" y="336" width="36" height="36" fill="var(--accent-green)"/>
      <text class="brand-name" x="860" y="364">LORNA PRATLEY</text>
    </g>

    <text class="agent-name" x="907" y="487" text-anchor="middle">LORNA PRATLEY</text>
    <text class="agent-role" x="907" y="507" text-anchor="middle">Realtor Harbor Sage Realty</text>

    <g class="contact-details">
      <text class="contact" x="881" y="591" text-anchor="end">(555) 418-2093</text>
      <rect class="icon-tile" x="885" y="574" width="21" height="21"/>
      <rect class="icon-line" x="892" y="578" width="7" height="13" rx="1"/>
      <rect class="icon-tile" x="915" y="574" width="21" height="21"/>
      <rect class="icon-line" x="918.5" y="580" width="14" height="9"/>
      <path class="icon-line" d="M918.5,580 L925.5,586 L932.5,580"/>
      <text class="contact-strong" x="939" y="589">lpratley@mailbarn.example</text>

      <text class="contact" x="883" y="622" text-anchor="end">BRE # 04872351  Exp. 8/15</text>
      <rect class="icon-tile" x="885" y="606" width="21" height="21"/>
      <path class="icon-line" d="M892,611 L890,622 M898,611 L896,622 M888,614.5 L901,614.5 M887.5,619 L900.5,619"/>
      <rect class="icon-tile" x="915" y="606" width="21" height="21"/>
      <circle class="icon-line" cx="925.5" cy="616.5" r="7"/>
      <ellipse class="icon-line" cx="925.5" cy="616.5" rx="3" ry="7"/>
      <path class="icon-line" d="M918.5,616.5 L932.5,616.5"/>
      <text class="contact-strong" x="939" y="621">www.lornanestfinder.example</text>
    </g>

    <text class="tagline" x="912" y="705" text-anchor="middle">"Where Keys Meet Kindred Spirits"</text>
  </g>
</svg>
</body>
</html>
```